Flyer for a Payroll and Bookkeeping Companmy

Need a brochure to highlight our costs and service to hand out to clients.

Please see attachments for more information.

Industry/Entity Type

It Service

```html
<!DOCTYPE html>
<html lang="en">
<head>
<meta charset="utf-8">
<title>Summit Ridge – Simplified Payroll Pricing</title>
<link href="https://fonts.googleapis.com/css2?family=Source+Sans+3:wght@400;600;700&display=swap" rel="stylesheet">
<style>
  :root {
    --page: #ffffff;
    --outer-frame: #e8a0a0;
    --inner-frame: #222222;
    --ink: #111111;
    --brand-blue: #1f6fb5;
    --brand-orange: #f08a2c;
    --orange-tab: #ef8c1f;
    --yellow-bar: #f7c21a;
    --olive-tab: #7e9a3a;
    --green-bar: #8dc63f;
    --blue-tab: #1f6db3;
    --cyan-bar: #22b6d8;
    --seal-red: #e42a34;
    --seal-red-deep: #c81d27;
    --white: #ffffff;
  }
  * { margin: 0; padding: 0; box-sizing: border-box; }
  html, body { width: 1200px; height: 942px; overflow: hidden; background: var(--page); }
  body { font-family: "Source Sans 3", "Myriad Pro", Arial, sans-serif; color: var(--ink); }

  .flyer { position: relative; width: 1200px; height: 942px; border: 1px solid var(--outer-frame); }
  .flyer__frame { position: absolute; left: 31px; top: 33px; width: 1137px; height: 879px; border: 1.5px solid var(--inner-frame); }

  .brand { position: absolute; left: 92px; top: 150px; }
  .brand__name { font-size: 25px; font-weight: 600; color: var(--brand-blue); line-height: 1; letter-spacing: -0.2px; }
  .brand__tagline { font-size: 14px; font-weight: 600; color: var(--brand-orange); margin-top: 3px; }

  .headline { position: absolute; left: 325px; top: 96px; font-size: 70px; font-weight: 600; color: var(--brand-orange); letter-spacing: -0.3px; line-height: 1; white-space: nowrap; }

  .rate { position: absolute; top: 238px; display: flex; align-items: center; }
  .rate__amount { font-size: 76px; font-weight: 700; line-height: 1; letter-spacing: -1px; }
  .rate__unit { font-size: 25px; font-weight: 700; line-height: 1.12; margin-left: 12px; }
  .rate--payroll { left: 305px; }
  .rate--employee { left: 686px; }
  .rate-plus { position: absolute; left: 593px; top: 250px; font-size: 48px; font-weight: 400; line-height: 1; }

  .terms { position: absolute; left: 0; top: 0; width: 760px; height: 942px; }
  .term__label { position: absolute; left: 94px; width: 204px; padding: 12px 0 0 10px; color: var(--white); font-size: 20px; font-weight: 700; line-height: 1.2; }
  .term__detail { position: absolute; left: 356px; color: var(--white); font-size: 16px; font-weight: 600; line-height: 1.1; }

  .seal { position: absolute; left: 767px; top: 392px; width: 354px; height: 354px; border-radius: 50%;
          background: radial-gradient(circle at 50% 45%, var(--seal-red) 60%, var(--seal-red-deep) 100%);
          display: flex; align-items: center; justify-content: center; }
  .seal__text { color: var(--white); font-size: 46px; font-weight: 600; line-height: 1.1; text-align: center; }

  .contact { position: absolute; left: 0; width: 1200px; top: 872px; text-align: center; font-size: 14.5px; font-weight: 600; word-spacing: 1px; }
  .contact__sep { margin: 0 8px; }
</style>
</head>
<body>
<main class="flyer">
  <div class="flyer__frame"></div>

  <div class="brand">
    <div class="brand__name">Summit Ridge</div>
    <div class="brand__tagline">Payroll and Bookkeeping</div>
  </div>

  <h1 class="headline">Simplified Payroll Pricing</h1>

  <div class="rate rate--payroll">
    <span class="rate__amount">$25</span>
    <span class="rate__unit">PER<br>PAYROLL</span>
  </div>
  <div class="rate-plus">+</div>
  <div class="rate rate--employee">
    <span class="rate__amount">$5</span>
    <span class="rate__unit">PER<br>EMPLOYEE</span>
  </div>

  <section class="terms">
    <svg class="terms__shapes" width="760" height="942" viewBox="0 0 760 942" aria-hidden="true">
      <defs>
        <filter id="soft-shadow" x="-20%" y="-20%" width="140%" height="160%">
          <feDropShadow dx="0" dy="3" stdDeviation="3" flood-color="#000" flood-opacity="0.3"/>
        </filter>
      </defs>
      <rect x="310" y="403" width="399" height="44" rx="22" fill="var(--yellow-bar)" filter="url(#soft-shadow)"/>
      <rect x="94" y="356" width="204" height="86" fill="var(--orange-tab)" filter="url(#soft-shadow)"/>
      <circle cx="294" cy="423" r="50" fill="var(--orange-tab)" filter="url(#soft-shadow)"/>
      <circle cx="294" cy="423" r="40" fill="var(--white)" filter="url(#soft-shadow)"/>
      <text x="294" y="433" text-anchor="middle" font-family="Source Sans 3, sans-serif" font-size="29" fill="#111">1</text>

      <rect x="310" y="557" width="399" height="45" rx="22" fill="var(--green-bar)" filter="url(#soft-shadow)"/>
      <rect x="94" y="508" width="204" height="88" fill="var(--olive-tab)" filter="url(#soft-shadow)"/>
      <circle cx="294" cy="578" r="50" fill="var(--olive-tab)" filter="url(#soft-shadow)"/>
      <circle cx="294" cy="578" r="40" fill="var(--white)" filter="url(#soft-shadow)"/>
      <text x="294" y="588" text-anchor="middle" font-family="Source Sans 3, sans-serif" font-size="29" fill="#111">2</text>

      <rect x="310" y="712" width="399" height="45" rx="22" fill="var(--cyan-bar)" filter="url(#soft-shadow)"/>
      <rect x="94" y="662" width="204" height="87" fill="var(--blue-tab)" filter="url(#soft-shadow)"/>
      <circle cx="294" cy="732" r="50" fill="var(--blue-tab)" filter="url(#soft-shadow)"/>
      <circle cx="294" cy="732" r="40" fill="var(--white)" filter="url(#soft-shadow)"/>
      <text x="294" y="742" text-anchor="middle" font-family="Source Sans 3, sans-serif" font-size="29" fill="#111">3</text>
    </svg>

    <div class="term__label" style="top:356px">DIRECT<br>DEPOSIT ONLY</div>
    <div class="term__detail" style="top:409px">ADD $20 PER PAYROLL IF YOU ELECT TO<br>HAVE PAPER CHECKS SHIPPED TO YOU</div>

    <div class="term__label" style="top:508px">MINIMUM<br>CHARGE</div>
    <div class="term__detail" style="top:571px">TWO PAYROLLS PER MONTH</div>

    <div class="term__label" style="top:662px">COST PER<br>EMPLOYEE</div>
    <div class="term__detail" style="top:726px">DROPS TO $4 AFTER 20 EMPLOYEES</div>
  </section>

  <div class="seal" role="img" aria-label="Red promotional seal announcing no set-up fees">
    <p class="seal__text">No Set-Up<br>Fees</p>
  </div>

  <footer class="contact">
    1480 W Harbor Ave, Cedar Falls, UT 84320<span class="contact__sep">•</span>555-014-2290<span class="contact__sep">•</span>SummitRidge.com
  </footer>
</main>
</body>
</html>
```